Fenwick and Torrance Postcard Design

Greetings!
Lawyers hire me as an expert witness. They take a gamble on hiring me in hopes of winning their case.
This postcard will be printed in jumbo size through Quillmark. The design must meet these specifications:

Full Bleed Size (starting document size)
11.12" x 6.12"
282 x 155 mm
3335 x 1835 pixels
* Finished artwork should use the full bleed dimensions for best results.
Document Trim Size (final size after being cut)
11.00" x 6.00"
279 x 152 mm
3300 x 1800 pixels
* Please be sure to keep all text and photos within the safe cutting margin.
Resolution
300 DPI
Visit Quillmark for more details or to download a design template:
https://www.quillmark-example.com/product-presentation-info.aspx?productPresentationId=1590#
https://www.quillmark-example.com/vp/ns/propath/UploadResources.aspx?selectedTab=0?pfid=BDW&pf_id=BDW&xnav=product-page#FileFormats

1. The postcard will have a Blank Backside.
2. I like a black, white and red color theme with a serious legalistic font.
3. In regards to color theme, see https://www.cardorbit-example.com/designs/security-system-postcards/#security-system-postcards-4
4. 8 preferred background images in alphabetical order from favorite to least favorite, but all are great:
a. https://files.driftbox-example.com/f/s!QwErTy12ZxCvBn34MnBvCx56LkJhGf
5. Header Text:
a. (line 1) Dr. K.R. Torrance, Psy.D., NCEB
b. (lines 2 and 3) Psychological Evaluator, Board-Certified Forensic Psychologist and National Expert Witness
c. (Line 4 in bold and more prominent than text in lines 1-3) 4 Signs of a Proficient & Credible Psyc. Expert
6. View this checklist image for inspiration, https://lnk.tidepoint-example.com/images/8RqWm3 and use the following text within such a checklist image:
7. Board Certified by the Continental Council of Courtroom Behavioral Science (CCCB)?
Yes, I'm Board Certified. This mark of proficiency in forensic psychology is recognized by judicial decisions, statutes and regulations.
8. Fellow of the Cont. Fellowship of Legal Behavioral Study?
Yes, I'm a CFLB Fellow, along with some of the field's most prominent leaders comprising the academic arm of the CCCB.
9. A Recognized Leader Amongst Other Experts?
I’m the 2018 duly elected President of the Hudson Valley Behavioral Guild Section on Courtroom Assessment, and a Board Member of the Coalition of Practitioners for Youth Safeguarding.
10. Positioned in Roles of Trust and Neutrality by Judges?
Yes, I work as an in-house Harborview Juvenile Tribunal mental-health expert in proceedings regarding competency, imminent risk, sentencing, custody, child maltreatment and TPR.
11. The following should be prominent along the bottom:
12. BOOK A LUNCH & LEARN AT YOUR OFFICE
Visit http://offer.witnessbench-example.com Call 555-014-2937
Designer: This call to action (CTA) for #12 needs to pop off of the page. It needs to draw the reader's eye. It needs depth, like the way a CTA button looks like on a website. Play around w/ idea to accomplish this (e.g., adding badges, icons, shapes, a picture, an image of someone presenting it, etc).
13. List my areas of specialization somewhere
• CPS & Matrimonial Issues
• Competency
• Juvenile Delinquency
• Criminal Sentencing
• Personal Injury and Civil Rights
• Immigration
• Fitness for Duty, SSD and Workers Comp
• Sex-Offenders
• IME and Neuropsychological Testing
• Behind-The-Scenes Consulting on A Contingency Fee
• Low-Price Initial Screening Evaluations
• Therapy Services & Programs for Litigants
14. Put this test somewhere and keep it subtle: I recognize the importance of your work. You can trust my assistance.
15. Put this in fine print somewhere (can be 2 lines): Fenwick and Torrance, LLC. 2018 New York Licensed Psychologist Lic. # 047213 - New Jersey Licensed Psychologist Lic. # 72K900315847

Target Market(s)

Lawyers

Industry/Entity Type

Hire

Font styles to use
Serif

Colors
ec1f27
ffffff

Requirements
Must have
• An awesome call to action. If the CTA doesn't catch the eye, then it won't work. The point of this postcard is to get them to that website so I can capture their email address. Anything else is a secondary gain. Consider 3-d design elements to give it pop and depth.
Should not have
• There's a big difference between a red rectangle and a red button on a website that has that 3d quality. This postcard has a lot of words. It can easily become just a bunch of text on a colorful piece of paper w/ a pic. Avoid this by segmenting the space, layering Diff color text on Diff color background and incorporating 3d design elements and shapes.

```html
<!DOCTYPE html>
<html lang="en">
<head>
<meta charset="utf-8">
<title>Fenwick and Torrance Postcard</title>
<link href="https://fonts.googleapis.com/css2?family=Montserrat:ital,wght@0,400;0,500;0,600;0,700;1,400;1,600;1,700&display=swap" rel="stylesheet">
<style>
  :root {
    --red: #ec1f27;
    --panel-red: #b70d0f;
    --deep-red: #7a0b0c;
    --black: #000000;
    --white: #ffffff;
    --ink: #2a2a2a;
    --edge: #3a3a3a;
    --footer: #d3d3d3;
    --stage: #ececec;
  }
  * { margin: 0; padding: 0; box-sizing: border-box; }
  html, body { width: 1200px; height: 1000px; overflow: hidden; }
  body { background: var(--stage); font-family: "Montserrat", Arial, sans-serif; position: relative; }

  .postcard {
    position: absolute; left: 55px; top: 177px;
    width: 1092px; height: 602px;
    background: var(--white); overflow: hidden;
  }
  .header {
    position: absolute; left: 0; top: 0; width: 100%; height: 110px;
    background: var(--black); color: var(--white); text-align: center;
  }
  .header__name { font-size: 36px; font-weight: 700; padding-top: 26px; letter-spacing: 0.3px; }
  .header__title { font-size: 15px; font-weight: 500; margin-top: 6px; }
  .header__rule { position: absolute; left: 0; top: 110px; width: 100%; height: 5px; background: var(--panel-red); }

  .courtroom-photo {
    position: absolute; left: 0; top: 118px; width: 100%; height: 427px;
    background: linear-gradient(100deg, #fbf7f2 0%, #f1e4d6 45%, #d9bfa3 70%, #c9a98a 100%);
  }

  .signs { position: absolute; left: 27px; top: 132px; width: 480px; }
  .signs__heading { color: var(--red); font-size: 19px; font-weight: 700; margin-bottom: 10px; }
  .sign { position: relative; padding-left: 18px; margin-bottom: 18px; font-size: 15px; line-height: 18.5px; }
  .sign__check { position: absolute; left: 0; top: 4px; width: 12px; height: 12px; }
  .sign__question { color: var(--red); font-weight: 700; }
  .sign__answer { color: var(--ink); font-style: italic; }

  .panel-shape { position: absolute; left: 0; top: 0; }

  .specialties { position: absolute; left: 628px; top: 145px; color: var(--white); }
  .specialties__heading { font-size: 19px; font-weight: 700; letter-spacing: 0.4px; margin: 0 0 10px 15px; }
  .specialties__grid { position: relative; width: 450px; height: 200px; }
  .specialties__col { position: absolute; top: 0; list-style: none; }
  .specialties__col--left { left: 0; width: 255px; }
  .specialties__col--right { left: 259px; width: 200px; }
  .specialty { position: relative; padding-left: 16px; font-size: 13px; font-weight: 500; line-height: 19.7px; text-transform: uppercase; white-space: nowrap; }
  .specialty::before { content: "\2714"; position: absolute; left: 0; top: 0; font-size: 12px; }

  .cta { position: absolute; left: 505px; top: 401px; width: 580px; height: 62px; }
  .cta__ribbon { position: absolute; left: 0; top: 0; }
  .cta__text { position: absolute; left: 40px; top: 7px; color: var(--white); white-space: nowrap; }
  .cta__headline { font-size: 19px; font-weight: 700; letter-spacing: 0.3px; }
  .cta__contact { font-size: 15px; font-weight: 700; margin-top: 3px; }
  .cta__contact span { color: #c9c9c9; font-weight: 500; }

  .assurance { position: absolute; left: 628px; top: 479px; color: var(--white); font-size: 19px; font-weight: 700; font-style: italic; line-height: 23px; text-align: center; width: 420px; }
  .assurance__mark { position: absolute; color: var(--deep-red); font-size: 56px; font-style: normal; font-family: Georgia, serif; line-height: 1; }
  .assurance__mark--open { left: -6px; top: -8px; }
  .assurance__mark--close { right: -26px; top: 14px; }

  .fine-print {
    position: absolute; left: 0; top: 545px; width: 100%; height: 57px;
    background: var(--footer); text-align: center; color: #5c5c5c;
    font-size: 13px; font-weight: 600; line-height: 17px; padding-top: 6px;
  }
  .fine-print strong { color: var(--black); font-weight: 700; }
</style>
</head>
<body>
<main class="postcard">
  <header class="header">
    <h1 class="header__name">Dr. K.R. Torrance, Psy.D., NCEB</h1>
    <p class="header__title">Psychological Evaluator, Board-Certified Forensic Psychologist &amp; National Expert Witness</p>
  </header>
  <div class="header__rule"></div>

  <div class="courtroom-photo" role="img" aria-label="Faded courtroom interior with wooden benches and scales of justice"></div>

  <svg class="panel-shape" width="1092" height="545" viewBox="0 0 1092 545" aria-hidden="true">
    <path d="M 480 545 L 600 150 Q 608 128 638 128 L 1092 128 L 1092 545 Z" fill="var(--edge)"/>
    <path d="M 493 545 L 613 150 Q 621 128 650 128 L 1092 128 L 1092 545 Z" fill="var(--panel-red)"/>
  </svg>

  <section class="signs">
    <h2 class="signs__heading">4 Signs of a Proficient &amp; Credible Psyc. Expert</h2>
    <p class="sign">
      <svg class="sign__check" viewBox="0 0 12 12" aria-hidden="true"><circle cx="6" cy="6" r="5" fill="none" stroke="#ec1f27" stroke-width="1.4"/><path d="M3.4 6.2 L5.4 8 L8.8 4.2" fill="none" stroke="#ec1f27" stroke-width="1.4"/></svg>
      <span class="sign__question">Board Certified by the Continental Council of Courtroom Behavioral Science (CCCB)?</span>
      <span class="sign__answer">Yes, I'm Board Certified. This mark of proficiency in forensic psychology is recognized by judicial decisions, statutes and regulations.</span>
    </p>
    <p class="sign">
      <svg class="sign__check" viewBox="0 0 12 12" aria-hidden="true"><circle cx="6" cy="6" r="5" fill="none" stroke="#ec1f27" stroke-width="1.4"/><path d="M3.4 6.2 L5.4 8 L8.8 4.2" fill="none" stroke="#ec1f27" stroke-width="1.4"/></svg>
      <span class="sign__question">Fellow of the Cont. Fellowship of Legal Behavioral Study?</span>
      <span class="sign__answer">Yes, I'm a CFLB Fellow, along with some of the field's most prominent leaders, comprising the academic arm of the CCCB.</span>
    </p>
    <p class="sign">
      <svg class="sign__check" viewBox="0 0 12 12" aria-hidden="true"><circle cx="6" cy="6" r="5" fill="none" stroke="#ec1f27" stroke-width="1.4"/><path d="M3.4 6.2 L5.4 8 L8.8 4.2" fill="none" stroke="#ec1f27" stroke-width="1.4"/></svg>
      <span class="sign__question">A Recognized Leader Amongst Other Experts?</span>
      <span class="sign__answer">I'm the 2018 duly elected President of the Hudson Valley Behavioral Guild Section on Courtroom Assessment, and a Board Member of the Coalition of Practitioners for Youth Safeguarding.</span>
    </p>
    <p class="sign">
      <svg class="sign__check" viewBox="0 0 12 12" aria-hidden="true"><circle cx="6" cy="6" r="5" fill="none" stroke="#ec1f27" stroke-width="1.4"/><path d="M3.4 6.2 L5.4 8 L8.8 4.2" fill="none" stroke="#ec1f27" stroke-width="1.4"/></svg>
      <span class="sign__question">Positioned in Roles of Trust and Neutrality by Judges?</span>
      <span class="sign__answer">Yes, I'm an in-house Harborview Juvenile Tribunal mental-health expert for proceedings regarding competency, imminent risk, sentencing, custody, child maltreatment and TPR.</span>
    </p>
  </section>

  <section class="specialties">
    <h2 class="specialties__heading">AREAS OF SPECIALIZATION</h2>
    <div class="specialties__grid">
      <ul class="specialties__col specialties__col--left">
        <li class="specialty">CPS &amp;Matrimonial Issues</li>
        <li class="specialty">Juvenile Delinquency</li>
        <li class="specialty">Personal Injury and<br>Civil Rights</li>
        <li class="specialty">Fitness for Duty, SSD and<br>Workers Comp</li>
        <li class="specialty">IME and Neuropsychological Testing</li>
        <li class="specialty">Behind-the-Scenes Consulting on a Contingency Fee</li>
        <li class="specialty">Low-Price Initial Screening Evaluations</li>
        <li class="specialty">Therapy Services and Programs for Litigants</li>
      </ul>
      <ul class="specialties__col specialties__col--right">
        <li class="specialty">Competency</li>
        <li class="specialty">Criminal Sentencing</li>
        <li class="specialty">Immigration</li>
        <li class="specialty">Sex-Offenders</li>
      </ul>
    </div>
  </section>

  <section class="cta">
    <svg class="cta__ribbon" width="580" height="62" viewBox="0 0 580 62" aria-hidden="true">
      <defs>
        <linearGradient id="ribbonShade" x1="0" y1="0" x2="0" y2="1">
          <stop offset="0" stop-color="#4a4a4a"/>
          <stop offset="0.45" stop-color="#151515"/>
          <stop offset="1" stop-color="#000000"/>
        </linearGradient>
      </defs>
      <path d="M 18 0 L 580 0 L 565 31 L 580 62 L 0 62 Z" fill="url(#ribbonShade)"/>
    </svg>
    <div class="cta__text">
      <p class="cta__headline">BOOK A LUNCH &amp; LEARN AT YOUR OFFICE</p>
      <p class="cta__contact"><span>Visit</span> http://offer.witnessbench-example.com <span>Call</span> 555-014-2937</p>
    </div>
  </section>

  <blockquote class="assurance">
    <span class="assurance__mark assurance__mark--open">&ldquo;</span>
    I recognize the importance of your<br>work. You can trust my assistance.
    <span class="assurance__mark assurance__mark--close">&rdquo;</span>
  </blockquote>

  <footer class="fine-print">
    <strong>FENWICK AND TORRANCE, LLC.</strong> 2018 NEW YORK LICENSED PSYCHOLOGIST LIC. # 047213 - NEW JERSEY<br>
    LICENSED PSYCHOLOGIST LIC. # 72K900315847
  </footer>
</main>
</body>
</html>
```